Veltrona Cabinets Letter Head and Email Signature

Hi
I would love a design package for a letterhead, email signature, even update my business card if you like if you can come up with a great idea for my new high end cabinet shop. Veltrona Cabinets brings timeless craftsmanship to modern interiors, specializing in high end, custom cabinetry designed for architects and interior designers.

Target Market(s)

high end, luxury market

Industry/Entity Type

cabinet making

Requirements
Must have
• my colours of logo as the theme

```html
<!DOCTYPE html>
<html lang="en">
<head>
<meta charset="utf-8">
<title>Veltrona Cabinets – Stationery</title>
<link rel="stylesheet" href="https://fonts.googleapis.com/css2?family=Montserrat:wght@400;500;600&display=swap">
<style>
:root{
  --green:#4a7c3f;
  --green-soft:#cfdccb;
  --ink:#111111;
  --black:#000000;
  --paper:#ffffff;
  --backdrop:#5b3520;
  --label:#ffffff;
}
*{box-sizing:border-box;margin:0;padding:0}
html,body{width:1131px;height:1200px;overflow:hidden}
body{background:var(--backdrop);font-family:'Montserrat',sans-serif;color:var(--ink);position:relative}
.abs{position:absolute}
.section-label{position:absolute;color:var(--label);font-size:16px;font-weight:500;letter-spacing:.3px}
.sheet{position:absolute;background:var(--paper)}
.brand{position:absolute;display:flex;align-items:center;gap:10px;color:var(--green);font-weight:500}
.brand .mark{border:2px solid currentColor;flex:none}
.brand .name{line-height:1}
.brand .name b{display:block;font-weight:500}
.brand .name span{display:block;font-weight:500;letter-spacing:.28em;margin-top:3px}
.row{position:absolute;display:flex;align-items:center;white-space:nowrap}
.item{display:flex;align-items:center;gap:5px}
.item svg{flex:none}
.person{color:var(--green);font-weight:600}
.role{font-size:6.5px;font-weight:500}
.tagline{color:var(--green)}
.on-dark{color:#fff}
.on-dark .item svg{stroke:#fff}
.icon{fill:none;stroke:var(--green);stroke-width:1.6;stroke-linecap:round;stroke-linejoin:round}
.icon-fill{fill:var(--green)}
</style>
</head>
<body>
<svg width="0" height="0" style="position:absolute">
  <defs>
    <symbol id="i-phone" viewBox="0 0 20 20"><circle cx="10" cy="10" r="8.5" class="icon"/><path class="icon" d="M7.5 6c-1 1.5-1 4.5 1.5 7 1 1 2.5 1.5 3.5 1l-1-2-1.2.5C9.2 11.5 8.5 10 8.7 8.8l1.1-.6L8.8 6z"/></symbol>
    <symbol id="i-mail" viewBox="0 0 20 16"><path class="icon-fill" d="M1 6l9-5 9 5v9H1z"/><path d="M3 7l7 4 7-4" fill="none" stroke="#fff" stroke-width="1.4"/></symbol>
    <symbol id="i-handle" viewBox="0 0 20 20"><circle cx="10" cy="10" r="8" class="icon"/></symbol>
    <symbol id="i-pin" viewBox="0 0 14 20"><path class="icon-fill" d="M7 0a6.5 6.5 0 0 0-6.5 6.5C.5 11.5 7 20 7 20s6.5-8.5 6.5-13.5A6.5 6.5 0 0 0 7 0zm0 9a2.5 2.5 0 1 1 0-5 2.5 2.5 0 0 1 0 5z"/></symbol>
  </defs>
</svg>

<!-- Letterhead -->
<div class="section-label" style="left:61px;top:27px">Letterhead</div>
<section class="sheet letterhead" style="left:60px;top:57px;width:599px;height:775px">
  <div class="brand" style="left:21px;top:19px">
    <div class="mark" style="width:34px;height:34px"></div>
    <div class="name"><b style="font-size:27px">Veltrona</b><span style="font-size:11px">CABINETS</span></div>
  </div>
  <div class="abs" style="right:15px;top:25px;text-align:right;font-size:11.5px;line-height:17px;letter-spacing:.2px">REFINED CRAFTSMANSHIP.<br>LASTING BEAUTY.</div>
  <div class="abs" style="left:597px;top:27px;width:2px;height:28px;background:var(--green)"></div>
  <footer class="abs on-dark" style="left:0;top:698px;width:599px;height:77px;background:var(--black);border-top:2px solid var(--green)">
    <div class="row" style="left:83px;top:10px;gap:44px;font-size:11.5px">
      <div class="item"><svg width="17" height="17"><use href="#i-phone"/></svg>040 555 0182</div>
      <div class="item"><svg width="18" height="14"><use href="#i-mail"/></svg>info@veltronacabinets.com.au</div>
      <div class="item"><svg width="17" height="17"><use href="#i-handle"/></svg>@veltrona.cabinets</div>
    </div>
    <div class="abs" style="left:160px;top:37px;width:326px;height:1px;background:#333"></div>
    <div class="row" style="left:192px;top:48px;font-size:11.5px">
      <div class="item"><svg width="11" height="15"><use href="#i-pin"/></svg>445 Street Name, City Name Australia 20854</div>
    </div>
  </footer>
</section>

<!-- Business card -->
<div class="section-label" style="left:923px;top:154px">Business Card</div>
<section class="sheet card-front" style="left:737px;top:192px;width:297px;height:169px;font-size:8.5px">
  <div class="person abs" style="left:16px;top:19px;font-size:12px">Marcus Halloran</div>
  <div class="role abs" style="left:16px;top:35px">Director Craftsman</div>
  <div class="abs" style="left:16px;top:62px;display:flex;flex-direction:column;gap:8px">
    <div class="item"><svg width="12" height="12"><use href="#i-phone"/></svg>040 555 0182</div>
    <div class="item"><svg width="12" height="10"><use href="#i-mail"/></svg>info@veltronacabinets.com.au</div>
    <div class="item"><svg width="12" height="12"><use href="#i-handle"/></svg>@veltrona.cabinets</div>
  </div>
  <div class="tagline abs" style="left:16px;top:137px;font-size:8px">Timeless Craft. Modern Interiors.</div>
</section>
<section class="sheet card-back" style="left:737px;top:380px;width:297px;height:169px;background:var(--black)">
  <div class="brand" style="left:53px;top:60px;gap:12px">
    <div class="mark" style="width:38px;height:38px"></div>
    <div class="name"><b style="font-size:31px">Veltrona</b><span style="font-size:13px">CABINETS</span></div>
  </div>
</section>

<!-- Email signature 1 -->
<section class="sheet sig-one" style="left:701px;top:623px;width:422px;height:168px;font-size:8px">
  <div class="brand" style="left:13px;top:12px;gap:8px">
    <div class="mark" style="width:26px;height:26px"></div>
    <div class="name"><b style="font-size:21px">Veltrona</b><span style="font-size:9px">CABINETS</span></div>
  </div>
  <div class="abs" style="left:13px;top:92px;font-size:10px"><span class="person">Marcus Halloran,</span> <span class="role" style="font-size:6.5px">Director Craftsman</span></div>
  <div class="row" style="left:13px;top:115px;gap:32px">
    <div class="item"><svg width="12" height="12"><use href="#i-phone"/></svg>040 555 0182</div>
    <div class="item"><svg width="13" height="10"><use href="#i-mail"/></svg>info@veltronacabinets.com.au</div>
    <div class="item"><svg width="12" height="12"><use href="#i-handle"/></svg>@veltrona.cabinets</div>
  </div>
  <div class="abs on-dark" style="left:0;top:141px;width:422px;height:27px;background:var(--black)">
    <div class="row" style="left:13px;top:7px"><div class="item"><svg width="8" height="11"><use href="#i-pin"/></svg>445 Street Name, City Name Australia 20854</div></div>
  </div>
</section>
<div class="section-label" style="left:707px;top:798px">Email Signature &nbsp;- Option 1</div>

<!-- Email signature 2 -->
<section class="sheet sig-two" style="left:33px;top:865px;width:456px;height:161px;font-size:8px">
  <div class="abs" style="left:0;top:0;width:175px;height:161px;background:var(--black)"></div>
  <div class="brand" style="left:14px;top:19px;gap:9px">
    <div class="mark" style="width:28px;height:28px"></div>
    <div class="name"><b style="font-size:22px">Veltrona</b><span style="font-size:9.5px">CABINETS</span></div>
  </div>
  <div class="abs" style="left:0;top:123px;width:456px;height:1px;background:#777"></div>
  <div class="tagline abs" style="left:13px;top:134px;font-size:8px">Timeless Craft. Modern Interiors.</div>
  <div class="person abs" style="left:196px;top:20px;font-size:11px">Marcus Halloran</div>
  <div class="role abs" style="left:196px;top:35px">Director Craftsman</div>
  <div class="abs" style="left:196px;top:60px;display:flex;flex-direction:column;gap:7px">
    <div class="item"><svg width="11" height="11"><use href="#i-phone"/></svg>040 555 0182</div>
    <div class="item"><svg width="12" height="9"><use href="#i-mail"/></svg>info@veltronacabinets.com.au</div>
    <div class="item"><svg width="11" height="11"><use href="#i-handle"/></svg>@veltrona.cabinets</div>
  </div>
  <div class="row" style="left:196px;top:134px"><div class="item"><svg width="10" height="13"><use href="#i-pin"/></svg>445 Street Name, City Name Australia 20854</div></div>
</section>
<div class="section-label" style="left:42px;top:1071px">Email Signature &nbsp;- Option 2</div>

<!-- Email signature 3 -->
<section class="sheet sig-three" style="left:496px;top:870px;width:602px;height:182px;font-size:8.5px">
  <div class="brand" style="left:17px;top:21px;gap:13px">
    <div class="mark" style="width:44px;height:44px"></div>
    <div class="name"><b style="font-size:32px">Veltrona</b><span style="font-size:13px">CABINETS</span></div>
  </div>
  <div class="abs" style="left:226px;top:29px;width:1px;height:127px;background:#ddd"></div>
  <div class="person abs" style="left:245px;top:21px;font-size:15px">Marcus Halloran</div>
  <div class="abs" style="left:245px;top:40px;font-size:8.5px;font-weight:500">Director Craftsman</div>
  <div class="abs" style="left:245px;top:56px;width:336px;height:1px;background:#ddd"></div>
  <div class="row" style="left:245px;top:66px;gap:14px">
    <div class="item"><svg width="13" height="13"><use href="#i-phone"/></svg>040 555 0182</div>
    <div class="item"><svg width="14" height="11"><use href="#i-mail"/></svg>info@veltronacabinets.com.au</div>
    <div class="item"><svg width="13" height="13"><use href="#i-handle"/></svg>@veltrona.cabinets</div>
  </div>
  <div class="abs" style="left:245px;top:93px;width:336px;height:1px;background:#ddd"></div>
  <div class="row" style="left:245px;top:103px"><div class="item"><svg width="9" height="12"><use href="#i-pin"/></svg>445 Street Name, City Name Australia 20854</div></div>
  <div class="abs" style="left:245px;top:128px;width:336px;height:1px;background:#ddd"></div>
  <div class="row" style="left:245px;top:140px;font-size:9.5px;font-weight:500;gap:20px">
    <div class="item"><svg width="15" height="15"><use href="#i-handle"/></svg>Circles</div>
    <div class="item"><svg width="15" height="15"><use href="#i-handle"/></svg>Profile</div>
    <div class="item"><svg width="15" height="15"><use href="#i-handle"/></svg>Pages</div>
    <div class="item"><svg width="15" height="15"><use href="#i-handle"/></svg>Gallery</div>
  </div>
</section>
<div class="section-label" style="left:496px;top:1071px">Email Signature &nbsp;- Option 3</div>
</body>
</html>
```